Yoga Workshop - Yoga Practice information flyer

I am a yoga teacher who will be presenting a workshop on yoga for sleep and need a brochure for my clients which outlines a practice that I give them so they can do the practice at home. Ideally I would like a brochure that is a single A3 size of paper in size that folds in half to an A4 booklet with the entire practice on the centre section to make it easy for people to do the practice at home with just one open page in front of them:
* Front page detailing "Yoga for Sleep Workshop" and "Restorative Yoga Practice"
* Centre contains the information on the practice contained in the attached word document. The practice consists of 5 postures, so there needs to be five separate sections which have the pictures of the postures (attached in uploaded files) and the wording contained in the attached word document. All pictures uploaded need to be included in the flyer as each posture has different pictures demonstrating the posture using yoga props or using things people have at home
* Back page containing a picture of myself (picture uploaded in files) with some information about me (contained in the attached word document) and my website www.lunavesperflow.com.au

I also need this flyer to be able to printed on 2 double sided A4 sheets of paper so will require 2 x pdf file versions. Importantly, for the centre section of the flyer, the design needs to ensure if it is printed on A4 paper, the wording and pictures for each of the postures are not separated over two pages

Target Market(s)

Existing clients

Requirements
Must have
• Detailed in project description
Nice to have
• The word document also contains some quotes. These do not need to be included in the flyer. If there is room and there is room for one or two of those please include where it would look good
Should not have
• Stock pictures of people in yoga postures which a normal everyday person could not get into

```html
<!DOCTYPE html>
<html lang="en">
<head>
<meta charset="utf-8">
<title>Yoga for Sleep Workshop – Restorative Yoga Practice Booklet</title>
<link href="https://fonts.googleapis.com/css2?family=Cinzel:wght@600;700&family=Open+Sans:wght@400;600;700&display=swap" rel="stylesheet">
<style>
:root{
  --canvas:#f2f2f2;
  --paper:#ffffff;
  --blush:#fbece5;
  --peach:#f2cdbb;
  --accent:#d8825a;
  --accent-deep:#c66e47;
  --title:#d88a68;
  --ink:#4d3a33;
  --muted:#8a7770;
  --line:#ecd3c6;
  --photo-a:#c9b8a6;
  --photo-b:#8fa0a8;
}
*{margin:0;padding:0;box-sizing:border-box}
html,body{width:1200px;height:2764px;overflow:hidden}
body{background:var(--canvas);font-family:"Open Sans",Arial,sans-serif;color:var(--ink);position:relative}
.spread{position:absolute;left:30px;width:1140px;height:806px;display:flex;background:var(--paper);box-shadow:0 6px 22px rgba(0,0,0,.12)}
.spread--outer{top:536px}
.spread--inner{top:1422px}
.page{width:570px;height:806px;position:relative;overflow:hidden}
.page + .page{border-left:1px solid #eee}
.serif{font-family:"Cinzel",Georgia,serif}
.photo{background:linear-gradient(160deg,var(--photo-a),var(--photo-b))}
.photo--circle{border-radius:50%;border:4px solid var(--paper);box-shadow:0 0 0 2px var(--accent)}
.band{display:inline-block;background:var(--accent);color:#fff;font-family:"Cinzel",Georgia,serif;font-weight:700;letter-spacing:1px}
.web{position:absolute;bottom:22px;left:0;right:0;text-align:center;font-size:10px;color:var(--muted);letter-spacing:.5px}

/* back page */
.back{background:linear-gradient(180deg,var(--blush) 0,var(--paper) 45%)}
.back__photo{position:absolute;left:175px;top:60px;width:220px;height:220px}
.back__heading{position:absolute;top:320px;width:100%;text-align:center;color:var(--accent);font-size:20px;font-weight:700;letter-spacing:2px}
.back__role{position:absolute;top:356px;left:0;right:0;text-align:center}
.back__role .band{font-size:12px;padding:5px 16px}
.back__bio{position:absolute;top:400px;left:70px;right:70px;text-align:center;font-size:10.5px;line-height:1.65;color:var(--ink)}
.back__contact{position:absolute;top:600px;width:100%;text-align:center;color:var(--accent);font-size:18px;font-weight:700;letter-spacing:2px}
.contact-row{position:absolute;top:645px;left:30px;right:30px;display:flex;justify-content:space-between;font-size:10px;color:var(--ink)}
.contact-row span{display:flex;align-items:center;gap:6px}
.contact-row svg{width:16px;height:16px}

/* front page */
.front{background:linear-gradient(180deg,var(--peach) 0,var(--blush) 35%,var(--paper) 70%)}
.brand{position:absolute;top:34px;width:100%;text-align:center}
.brand__dot{width:22px;height:22px;border-radius:50%;background:var(--accent);margin:0 auto 6px}
.brand__name{font-family:"Cinzel",Georgia,serif;font-weight:700;font-size:18px;color:var(--accent)}
.brand__tag{font-size:8px;color:var(--muted);margin-top:3px;letter-spacing:.5px}
.front__photo{position:absolute;left:160px;top:130px;width:250px;height:250px}
.front__title{position:absolute;top:440px;width:100%;text-align:center;font-family:"Cinzel",Georgia,serif;font-weight:700;line-height:1.05}
.front__title .l1{font-size:38px;color:var(--title)}
.front__title .l2{font-size:40px;color:var(--ink)}
.front__sub{position:absolute;top:548px;width:100%;text-align:center}
.front__sub .band{font-size:20px;padding:8px 22px}

/* inner pages */
.inner{padding:28px 30px 50px}
.intro{font-size:9.5px;line-height:1.55;margin-bottom:14px}
.posture{margin-bottom:16px}
.posture__head{display:block;font-size:11px;padding:5px 10px;margin-bottom:8px}
.posture__body{display:flex;gap:12px}
.posture__text{flex:1;font-size:9px;line-height:1.55}
.posture__photos{display:flex;gap:6px}
.posture__photos .photo{width:70px;height:92px}
.quote{display:flex;align-items:center;gap:14px;border:1px solid var(--line);background:var(--blush);padding:10px 14px;margin-bottom:10px}
.quote__mark{font-family:"Cinzel",Georgia,serif;font-size:40px;line-height:1;color:var(--accent);font-weight:700}
.quote__text{font-family:"Cinzel",Georgia,serif;font-size:11.5px;font-weight:600;line-height:1.45;color:var(--ink)}
.quote__by{display:block;font-family:"Open Sans",Arial,sans-serif;font-size:8.5px;font-weight:400;color:var(--accent);margin-top:3px}
</style>
</head>
<body>

<section class="spread spread--outer">
  <article class="page back">
    <div class="photo photo--circle back__photo" role="img" aria-label="Portrait of the yoga teacher seated cross-legged outdoors"></div>
    <h2 class="back__heading serif">MEET LUNA VESPER</h2>
    <div class="back__role"><span class="band">Restorative Yoga Teacher</span></div>
    <p class="back__bio">I have been practising yoga for many years and teaching gentle and restorative classes to help people slow down, rest and reconnect. My aim is to share simple practices you can enjoy at home, using props or everyday items, so that calm and good sleep become part of daily life. I look forward to practising with you again soon.</p>
    <h3 class="back__contact serif">CONTACT US</h3>
    <div class="contact-row">
      <span><svg viewBox="0 0 16 16"><circle cx="8" cy="8" r="8" fill="#d8825a"/><path d="M5.2 4.2l1.4-.3.8 1.9-.9.7a5 5 0 002.9 2.9l.7-.9 1.9.8-.3 1.4c-3.6.2-6.7-2.9-6.5-6.5z" fill="#fff"/></svg>0400 318 562</span>
      <span><svg viewBox="0 0 16 16"><circle cx="8" cy="8" r="8" fill="#d8825a"/><rect x="4" y="5" width="8" height="6" fill="none" stroke="#fff"/><path d="M4 5l4 3 4-3" fill="none" stroke="#fff"/></svg>hello@lunavesperflow.com.au</span>
      <span><svg viewBox="0 0 16 16"><circle cx="8" cy="8" r="8" fill="#d8825a"/><circle cx="8" cy="8" r="4" fill="none" stroke="#fff"/><path d="M4 8h8M8 4v8" stroke="#fff"/></svg>www.lunavesperflow.com.au</span>
    </div>
  </article>
  <article class="page front">
    <div class="brand">
      <div class="brand__dot"></div>
      <div class="brand__name">Luna Vesper</div>
      <div class="brand__tag">Yoga for rest, breath and balance</div>
    </div>
    <div class="photo photo--circle front__photo" role="img" aria-label="Woman meditating cross-legged on a yoga mat at home"></div>
    <h1 class="front__title"><span class="l1">YOGA FOR</span><br><span class="l2">SLEEP WORKSHOP</span></h1>
    <div class="front__sub"><span class="band">RESTORATIVE YOGA PRACTICE</span></div>
    <div class="web">www.lunavesperflow.com.au</div>
  </article>
</section>

<section class="spread spread--inner">
  <article class="page inner">
    <p class="intro">This gentle practice helps the body and mind settle before bed. Move slowly, breathe softly through the nose and stay in each posture for three to five minutes. Use bolsters, blankets or cushions from around your home, and let each shape feel fully supported and easy.</p>
    <div class="posture">
      <span class="band posture__head">Posture 1 – Supported Child's Pose</span>
      <div class="posture__body">
        <p class="posture__text">Kneel with knees wide and place a bolster or pillows lengthwise between the legs. Fold forward and rest the chest and one cheek on the support. Let the arms relax and breathe into the back of the body.</p>
        <div class="posture__photos">
          <div class="photo" role="img" aria-label="Child's pose over a bolster"></div>
          <div class="photo" role="img" aria-label="Child's pose over pillows"></div>
        </div>
      </div>
    </div>
    <div class="posture">
      <span class="band posture__head">Posture 2 – Supported Forward Fold</span>
      <div class="posture__body">
        <p class="posture__text">Sit with legs extended and rest the forehead on a chair seat or stacked cushions. Keep the spine long and soft. Allow the breath to slow down and the shoulders to melt away from the ears.</p>
        <div class="posture__photos">
          <div class="photo" role="img" aria-label="Seated forward fold onto a chair"></div>
          <div class="photo" role="img" aria-label="Seated forward fold onto cushions"></div>
        </div>
      </div>
    </div>
    <div class="posture">
      <span class="band posture__head">Posture 3 – Supported Reclining Twist</span>
      <div class="posture__body">
        <p class="posture__text">Lie on your back, draw the knees in and lower them to one side onto a folded blanket. Open the arms and turn the head gently. Stay a few minutes, then change sides slowly.</p>
        <div class="posture__photos">
          <div class="photo" role="img" aria-label="Reclining twist with blanket"></div>
          <div class="photo" role="img" aria-label="Reclining twist with cushion"></div>
        </div>
      </div>
    </div>
    <div class="web">www.lunavesperflow.com.au</div>
  </article>
  <article class="page inner">
    <div class="posture">
      <span class="band posture__head">Posture 4 – Legs Up the Wall</span>
      <div class="posture__body">
        <p class="posture__text">Sit side-on to a wall, then swing the legs up as you lie back. Place a folded blanket under the hips if you like. Rest the hands on the belly and feel it rise and fall.</p>
        <div class="posture__photos">
          <div class="photo" role="img" aria-label="Legs up the wall with blanket"></div>
          <div class="photo" role="img" aria-label="Legs resting on a couch"></div>
        </div>
      </div>
    </div>
    <div class="posture">
      <span class="band posture__head">Posture 5 – Supported Relaxation</span>
      <div class="posture__body">
        <p class="posture__text">Lie on your back with a pillow under the knees and a folded blanket under the head. Cover yourself to stay warm and let the whole body become heavy and still.</p>
        <div class="posture__photos">
          <div class="photo" role="img" aria-label="Relaxation pose with bolster under knees"></div>
          <div class="photo" role="img" aria-label="Relaxation pose under a blanket"></div>
        </div>
      </div>
    </div>
    <div class="quote"><span class="quote__mark">“</span><p class="quote__text">Posture should be steady and comfortable.<span class="quote__by">~ Ancient yoga teaching</span></p></div>
    <div class="quote"><span class="quote__mark">“</span><p class="quote__text">Rest is not idleness, it is the ground from which we grow.<span class="quote__by">~ Unknown</span></p></div>
    <div class="quote"><span class="quote__mark">“</span><p class="quote__text">Slow breath, quiet mind, restful night.<span class="quote__by">~ Unknown</span></p></div>
    <div class="quote"><span class="quote__mark">“</span><p class="quote__text">Watch your breath, it becomes your calm. Watch your calm, it becomes your sleep.<span class="quote__by">~ Unknown</span></p></div>
    <div class="web">www.lunavesperflow.com.au</div>
  </article>
</section>

</body>
</html>
```